Marrowfield Contracting Business Cards

Front of card:

Full Logo
Name
Address
Office Phone
Cell Phone
Email
Website

Back:
Logo Mark in background
List and markets and services performed

```html
<!DOCTYPE html>
<html lang="en">
<head>
<meta charset="utf-8">
<title>Marrowfield Contracting Business Cards</title>
<link href="https://fonts.googleapis.com/css2?family=Roboto:wght@400;700&display=swap" rel="stylesheet">
<style>
  :root {
    --backdrop: #2b2b2b;
    --brand-red: #d62428;
    --card-white: #ffffff;
    --ink-grey: #6e6e6e;
    --rule-grey: #8a8a8a;
  }
  html, body {
    margin: 0;
    padding: 0;
    width: 1200px;
    height: 959px;
    overflow: hidden;
    background: var(--backdrop);
    font-family: "Roboto", Arial, sans-serif;
  }
  .stage { position: relative; width: 1200px; height: 959px; }
  .card {
    position: absolute;
    width: 525px;
    height: 300px;
    border-radius: 16px;
    box-shadow: 0 10px 24px rgba(0,0,0,0.45);
    box-sizing: border-box;
  }
  /* back */
  .card-back {
    left: 90px; top: 130px;
    background: var(--brand-red);
    color: var(--card-white);
    display: flex; flex-direction: column;
    align-items: center; justify-content: center;
    gap: 26px;
  }
  .back-brand { display: flex; align-items: center; gap: 14px; }
  .back-brand .dot { width: 34px; height: 34px; border-radius: 50%; background: var(--card-white); }
  .back-brand .name { font-weight: 700; font-size: 30px; letter-spacing: 0.5px; }
  .services { font-size: 15px; letter-spacing: 0.3px; }
  /* front */
  .card-front {
    left: 585px; top: 520px;
    background: var(--card-white);
    display: flex; align-items: center;
    padding: 0 30px;
  }
  .front-brand { width: 215px; display: flex; flex-direction: column; align-items: center; gap: 14px; }
  .front-brand .dot { width: 58px; height: 58px; border-radius: 50%; background: var(--brand-red); }
  .front-brand .name {
    font-weight: 700; font-size: 24px; line-height: 1.15;
    color: var(--brand-red); text-align: center; text-transform: uppercase;
    padding-bottom: 8px; border-bottom: 1.5px solid var(--rule-grey);
  }
  .divider { width: 1.5px; height: 120px; background: var(--rule-grey); margin: 0 22px 0 14px; }
  .contact { color: var(--ink-grey); font-size: 12px; line-height: 1.45; }
  .contact .person { color: var(--brand-red); font-weight: 700; font-size: 19px; text-transform: uppercase; line-height: 1.1; }
  .contact .role { font-size: 12.5px; margin-bottom: 8px; }
  .contact .address { margin-bottom: 8px; }
  .contact ul { list-style: none; margin: 0; padding: 0; }
  .contact li { display: flex; align-items: center; gap: 6px; }
  .contact svg { width: 10px; height: 10px; flex: none; fill: var(--brand-red); }
</style>
</head>
<body>
<div class="stage">
  <section class="card card-back">
    <div class="back-brand">
      <span class="dot"></span>
      <span class="name">Marrowfield Contracting</span>
    </div>
    <p class="services">List and markets and services performed</p>
  </section>

  <section class="card card-front">
    <div class="front-brand">
      <span class="dot"></span>
      <span class="name">Marrowfield<br>Contracting</span>
    </div>
    <div class="divider"></div>
    <div class="contact">
      <div class="person">Daniel Okafor</div>
      <div class="role">Founder</div>
      <div class="address">48 Harlow Street, Ground Floor<br>Brookvale, NY 10417</div>
      <ul>
        <li><svg viewBox="0 0 10 10"><path d="M2 0.5 L4 2.5 L3 3.6 Q4.2 5.8 6.4 7 L7.5 6 L9.5 8 L8 9.5 Q4 9.5 0.5 2 Z"/></svg>(555) 210-4471</li>
        <li><svg viewBox="0 0 10 10"><path d="M2.5 0 H7.5 V10 H2.5 Z M3.5 1 V8 H6.5 V1 Z"/></svg>(555) 210-4472</li>
        <li><svg viewBox="0 0 10 10"><path d="M0 2 H10 V8 H0 Z M0.8 2.6 L5 5.6 L9.2 2.6 Z" fill-rule="evenodd"/></svg>info@MarrowfieldContracting.com</li>
        <li><svg viewBox="0 0 10 10"><circle cx="5" cy="5" r="4.5"/></svg>www.MarrowfieldContracting.com</li>
      </ul>
    </div>
  </section>
</div>
</body>
</html>
```